Quote Cards With KB May 2025 for Instagram

I would like to put these quotes over one of the pictures attached; Instagram (new size: 4:5 (1080 x 1350 pixels) One Quote per picture, and I want the quote to be bold or easy to read as well. I provided a few reference graphics that I really like as examples below. In very small letters at the bottom add @KimBarlowDaily

All of the pictures are attached; you can pick any photo and add one quote to it; but no stock photography

```html
<!DOCTYPE html>
<html lang="en">
<head>
<meta charset="utf-8">
<title>Quote Card – KB</title>
<link href="https://fonts.googleapis.com/css2?family=Bebas+Neue&display=swap" rel="stylesheet">
<style>
  :root {
    --bg-dark: #161616;
    --bg-mid: #2a2a2a;
    --band: #29b8d6;
    --quote-red: #d9453f;
    --text: #ffffff;
    --ghost: rgba(120, 120, 120, 0.35);
    --photo-light: #8a8a8a;
    --photo-dark: #1f1f1f;
  }
  * { margin: 0; padding: 0; box-sizing: border-box; }
  html, body { width: 960px; height: 1200px; overflow: hidden; background: var(--bg-dark); }
  .card {
    position: relative;
    width: 960px;
    height: 1200px;
    overflow: hidden;
    background: radial-gradient(ellipse at 40% 45%, var(--bg-mid) 0%, var(--bg-dark) 75%);
    font-family: "Bebas Neue", "Arial Narrow", sans-serif;
    color: var(--text);
  }
  .accent-band {
    position: absolute;
    left: 0; top: 277px;
    width: 960px; height: 269px;
    background: var(--band);
  }
  .ghost-handle {
    position: absolute;
    left: 570px; top: 70px;
    font-size: 150px;
    line-height: 1;
    color: var(--ghost);
    white-space: nowrap;
    transform-origin: 0 0;
    transform: rotate(90deg) translateY(-150px);
    letter-spacing: 1px;
  }
  .portrait {
    position: absolute;
    left: 210px; top: 100px;
    width: 670px; height: 1100px;
    border-radius: 300px 300px 40px 40px;
    background: linear-gradient(180deg, var(--photo-light) 0%, #555 30%, var(--photo-dark) 70%, #141414 100%);
    opacity: 0.9;
  }
  .quote-mark {
    position: absolute;
    left: 122px; top: 640px;
    width: 62px; height: 44px;
  }
  .quote-text {
    position: absolute;
    left: 124px; top: 735px;
    font-size: 54px;
    line-height: 67px;
    letter-spacing: 0.2px;
  }
  .handle {
    position: absolute;
    left: 124px; top: 1044px;
    font-size: 30px;
    letter-spacing: 0.3px;
  }
</style>
</head>
<body>
  <main class="card">
    <div class="accent-band"></div>
    <div class="ghost-handle" aria-hidden="true">@KIMBARLOWDAILY</div>
    <div class="portrait" role="img" aria-label="Black and white portrait of a smiling woman with long wavy hair in a black sheer long-sleeve top, hand on hip"></div>

    <svg class="quote-mark" viewBox="0 0 62 44" aria-hidden="true">
      <path fill="var(--quote-red)" d="M0 44V26C0 12 6 3 20 0l2 6c-7 3-10 8-10 14h10v24H0Z"/>
      <path fill="var(--quote-red)" d="M36 44V26C36 12 42 3 56 0l2 6c-7 3-10 8-10 14h10v24H36Z"/>
    </svg>

    <p class="quote-text">
      What worked in<br>
      your 30s won’t work now.<br>
      Here’s what actually does.<br>
      Drop 30 pounds in 3 months.
    </p>

    <p class="handle">@KimBarlowDaily</p>
  </main>
</body>
</html>
```